Ambushed

A lady is ambushed by two males in a pickup truck using VR-19s.
She is wearing female business attire going to work. Eloquent clothes representative of a person in her position, Director of her department.

Below is the scene describing the ambush. The female character, Lorena, is 5'9", 135lbs, brown hair. Her car is a Kestra 7, four door, gun metal gray, 2014.

```html
<!DOCTYPE html>
<html lang="en">
<head>
<meta charset="utf-8">
<title>Ambushed — Book Cover</title>
<link rel="stylesheet" href="https://fonts.googleapis.com/css2?family=Anton&family=Crimson+Text:ital,wght@1,700&family=Montserrat:wght@700&display=swap">
<style>
  :root {
    --page-bg: #f6d2a9;
    --cover-black: #050607;
    --cyan-light: #5fe3f5;
    --cyan-mid: #1ab6d8;
    --cyan-deep: #0a6f9c;
    --tagline-blue: #1a9ccc;
    --haze-warm: #8a6a45;
    --haze-teal: #4d5c5c;
    --gunmetal: #55585a;
    --shadow-dark: #1d2224;
  }
  * { box-sizing: border-box; margin: 0; padding: 0; }
  html, body {
    width: 1200px;
    height: 900px;
    overflow: hidden;
    background: var(--page-bg);
  }
  .canvas {
    position: relative;
    width: 1200px;
    height: 900px;
    display: flex;
    align-items: center;
    justify-content: center;
  }
  .book-cover {
    position: relative;
    width: 512px;
    height: 820px;
    background: var(--cover-black);
    overflow: hidden;
  }
  .cover-scene {
    position: absolute;
    inset: 0 0 auto 0;
    height: 590px;
    background:
      radial-gradient(ellipse 45% 30% at 12% 18%, rgba(214, 150, 80, 0.75), transparent 70%),
      radial-gradient(ellipse 40% 25% at 80% 12%, rgba(170, 190, 185, 0.55), transparent 70%),
      radial-gradient(ellipse 70% 30% at 55% 62%, rgba(110, 114, 116, 0.9), transparent 75%),
      linear-gradient(180deg, var(--haze-warm) 0%, var(--haze-teal) 28%, var(--shadow-dark) 45%, var(--gunmetal) 62%, #2a2d2f 78%, var(--cover-black) 100%);
  }
  .title-flare {
    position: absolute;
    left: 20px;
    right: 20px;
    top: 548px;
    height: 2px;
    background: linear-gradient(90deg, transparent, rgba(200, 230, 255, 0.9) 50%, transparent);
  }
  .book-title {
    position: absolute;
    left: 56px;
    top: 500px;
    width: 400px;
    height: 124px;
    font-size: 0;
  }
  .book-title svg {
    display: block;
    width: 400px;
    height: 124px;
    overflow: visible;
  }
  .book-title text {
    font-family: "Anton", sans-serif;
    font-size: 158px;
  }
  .tagline {
    position: absolute;
    left: 30px;
    right: 30px;
    top: 654px;
    text-align: center;
    font-family: "Crimson Text", serif;
    font-style: italic;
    font-weight: 700;
    font-size: 19.5px;
    line-height: 23px;
    letter-spacing: 0.6px;
    color: var(--tagline-blue);
  }
  .author-name {
    position: absolute;
    left: 0;
    right: 0;
    top: 773px;
    text-align: center;
    font-family: "Montserrat", sans-serif;
    font-weight: 700;
    font-size: 24px;
    line-height: 1;
    letter-spacing: 0.42em;
    padding-left: 0.42em;
    color: var(--cyan-mid);
  }
</style>
</head>
<body>
  <main class="canvas">
    <article class="book-cover">
      <div class="cover-scene" role="img" aria-label="Night car park in haze: two armed men with VR-19s crouch in a pickup bed behind a gunmetal gray Kestra 7, while Lorena, in a navy business suit, raises her hands in alarm"></div>
      <div class="title-flare"></div>
      <h1 class="book-title" aria-label="Ambushed">
        <svg viewBox="0 0 400 124" aria-hidden="true">
          <defs>
            <linearGradient id="title-fill" x1="0" y1="0" x2="0" y2="1">
              <stop offset="0" stop-color="#5fe3f5"/>
              <stop offset="0.5" stop-color="#1ab6d8"/>
              <stop offset="1" stop-color="#0a6f9c"/>
            </linearGradient>
            <pattern id="title-lines" width="6" height="5" patternUnits="userSpaceOnUse">
              <rect width="6" height="2" fill="rgba(0,0,0,0.4)"/>
            </pattern>
          </defs>
          <text x="0" y="122" textLength="400" lengthAdjust="spacingAndGlyphs" fill="url(#title-fill)">AMBUSHED</text>
          <text x="0" y="122" textLength="400" lengthAdjust="spacingAndGlyphs" fill="url(#title-lines)">AMBUSHED</text>
        </svg>
      </h1>
      <p class="tagline">Lorem ipsum dolor sit amet, consectetur<br>adipiscing elit, Quis ipsum suspendisse<br>ultrices gravida.</p>
      <p class="author-name">AUTHOR NAME</p>
    </article>
  </main>
</body>
</html>
```